Business card for Mortgage broker business

I have already had the logo designed and am needing a great looking business card. My business focus is on servicing clients who may not be able to obtain finance through traditional lenders due to bad credit, short term employment or they just don't fit the banks profile. It needs to be professional, trust worthy but also have a caring fell about it.
I have provided files showing the green and black logo, the white logo(on white background so the file looks blank) and also a file with the white logo with a background of leaves that was made up which will probably be used for a website header.

Industry/Entity Type

Finance

Contact Information for Business Card

Marcus Dolbey
Managing Director, Accredited Finance Broker(AFB)
Po Box 287, Pakenham VIC 3810
marcus@kestrelfinance.com.au
www.kestrelfinance.com.au
0438 162 507

Requirements
Nice to have
• I have added a picture of myself as I would like to see some designs with the pic in it, but I'm not sure if I want it on there with the logo's or just the logo's

```html
<!DOCTYPE html>
<html lang="en">
<head>
<meta charset="utf-8">
<title>Kestrel Finance – Business Card</title>
<link href="https://fonts.googleapis.com/css2?family=Lato:wght@300;400;700&display=swap" rel="stylesheet">
<style>
  :root {
    --page-bg: #eeedeb;
    --card-dark: #1b1f25;
    --card-mid: #2f353d;
    --panel-light: #4b5159;
    --rule: #4a5158;
    --white: #ffffff;
    --muted: #4e555d;
    --icon: #2c3138;
  }
  * { margin: 0; padding: 0; box-sizing: border-box; }
  html, body {
    width: 1200px; height: 1200px; overflow: hidden;
    background: var(--page-bg);
    font-family: "Lato", sans-serif;
  }
  .card {
    position: absolute;
    left: 210px;
    width: 780px;
    height: 445px;
    overflow: hidden;
    box-shadow: 0 6px 18px rgba(0,0,0,0.18);
  }
  /* Front */
  .card-front {
    top: 122px;
    background: linear-gradient(200deg, var(--card-dark) 0%, var(--card-mid) 100%);
  }
  .front-rule {
    position: absolute;
    top: 233px;
    height: 2px;
    background: var(--rule);
  }
  .front-rule.left { left: 0; width: 226px; }
  .front-rule.right { right: 0; width: 219px; }
  .brand-name {
    position: absolute;
    left: 226px;
    width: 335px;
    top: 210px;
    text-align: center;
    color: var(--white);
    font-weight: 300;
    font-size: 24px;
    letter-spacing: 3px;
    text-transform: uppercase;
    line-height: 48px;
    white-space: nowrap;
  }
  /* Back */
  .card-back {
    top: 632px;
    background: var(--white);
  }
  .portrait {
    position: absolute;
    left: 0; top: 0;
    width: 348px; height: 445px;
    background: linear-gradient(180deg, #ffffff 0%, #ffffff 24%, #c9a58c 45%, #8a6a58 62%, #2f3138 82%, #25272c 100%);
  }
  .name-band {
    position: absolute;
    left: 348px; top: 0;
    width: 432px; height: 115px;
    background: linear-gradient(90deg, var(--card-mid) 0%, var(--card-dark) 100%);
    padding: 16px 0 0 36px;
  }
  .person-name {
    color: var(--white);
    font-size: 44px;
    line-height: 52px;
    font-weight: 300;
    white-space: nowrap;
  }
  .person-name strong { font-weight: 700; }
  .person-title {
    color: var(--muted);
    font-size: 15px;
    font-weight: 300;
    margin-top: 6px;
    white-space: nowrap;
  }
  .icon-strip {
    position: absolute;
    left: 348px; top: 115px;
    width: 54px; height: 231px;
    background: var(--white);
  }
  .icon {
    position: absolute;
    left: 10px;
    width: 28px; height: 28px;
  }
  .contact-panel {
    position: absolute;
    left: 402px; top: 115px;
    width: 378px; height: 231px;
    background: linear-gradient(90deg, var(--panel-light) 0%, var(--card-mid) 100%);
  }
  .contact-line {
    position: absolute;
    left: 28px;
    color: var(--white);
    font-size: 16.5px;
    font-weight: 400;
    white-space: nowrap;
  }
  .footer-band {
    position: absolute;
    left: 348px; top: 346px;
    width: 432px; height: 99px;
    background: linear-gradient(90deg, var(--card-mid) 0%, var(--card-dark) 60%, #121519 100%);
  }
</style>
</head>
<body>

<section class="card card-front">
  <div class="front-rule left"></div>
  <div class="front-rule right"></div>
  <div class="brand-name">Kestrel Finance</div>
</section>

<section class="card card-back">
  <div class="portrait" role="img" aria-label="Portrait photo of Marcus Dolbey in a dark suit"></div>

  <header class="name-band">
    <h1 class="person-name">Marcus <strong>Dolbey</strong></h1>
    <p class="person-title">Managing Director, Accredited Finance Broker(AFB)</p>
  </header>

  <div class="icon-strip">
    <svg class="icon" style="top:51px" viewBox="0 0 28 28" aria-hidden="true">
      <rect x="2" y="7" width="24" height="15" fill="var(--icon)"/>
      <path d="M2 7 L14 16 L26 7 M2 22 L11 14 M26 22 L17 14" stroke="var(--white)" stroke-width="1.6" fill="none"/>
    </svg>
    <svg class="icon" style="top:107px" viewBox="0 0 28 28" aria-hidden="true">
      <circle cx="14" cy="14" r="13" fill="var(--icon)"/>
      <path d="M14 7 a4.5 4.5 0 0 1 4.5 4.5 c0 3.2 -4.5 7.5 -4.5 7.5 s-4.5 -4.3 -4.5 -7.5 A4.5 4.5 0 0 1 14 7 z" fill="none" stroke="var(--white)" stroke-width="1.5"/>
      <circle cx="14" cy="11.5" r="1.6" fill="var(--white)"/>
      <ellipse cx="14" cy="20.5" rx="5" ry="1.3" fill="none" stroke="var(--white)" stroke-width="1.2"/>
    </svg>
    <svg class="icon" style="top:164px" viewBox="0 0 28 28" aria-hidden="true">
      <circle cx="14" cy="14" r="13" fill="var(--icon)"/>
      <circle cx="14" cy="14" r="8.5" fill="none" stroke="var(--white)" stroke-width="1.4"/>
      <path d="M8 10 c3 1 4 -1 6 1 s-1 4 2 5 M15 6 c-1 2 1 3 3 3 M10 19 c1 -2 3 -1 3 1" fill="none" stroke="var(--white)" stroke-width="1.4"/>
    </svg>
  </div>

  <div class="contact-panel">
    <p class="contact-line" style="top:54px">marcus@kestrelfinance.com.au</p>
    <p class="contact-line" style="top:111px">Po Box 287, Pakenham VIC 3810</p>
    <p class="contact-line" style="top:168px">www.kestrelfinance.com.au</p>
  </div>

  <div class="footer-band"></div>
</section>

</body>
</html>
```